Nobody Left the Lantern Burning - Tom Halvery - CD Cover Design Project

Single Cover for CD & Online media e.g. Tunebox Graphics
The first song release from Tom Halvery will be the track 'Nobody Left the Lantern Burning'.
For the release the single requires artwork that is eye catching, seriously professional & meets the requirements of Disc Sprout, Tunebox and also a physical copy on CD.
Track listings for CD will be:
1. Nobody Left the Lantern Burning
2. Nobody Left the Lantern Burning - Instrumental
see details in this link:
http://members.discsprout-example.com/faq.aspx
http://selfmadesound.discsprout-example.com/2009/11/avoid-album-art-atrocities/
http://answers.quorvex-example.com/question/index?qid=20111015141433AAdDTmH
Any advice on this would be greatly appreciated,
I would also like the two logo's I have uploaded to be used,
one is the Tom Halvery logo and the other is for Milbrook & Tandy Records logo (please remove the R and replace with a C for copyright.)
There are four high res photo shopped pictures of Tom Halvery and another zip file of many others, it would be nice to include one of these maybe on the 2nd page or back of the CD. Please don't use them as the front cover.
I imagine an Art Deco illustration but please listen to the track and let it inspire you.
Good Luck
Updates
I don't feel this is what I'm looking for, the design needs to refelct a broken heart without being a picture of a broken heart
Reason: No design has been what we are after so far so the deadline has been extended and the budget increased.

```html
<!DOCTYPE html>
<html lang="en">
<head>
<meta charset="utf-8">
<title>Nobody Left the Lantern Burning – Tom Halvery</title>
<link rel="stylesheet" href="https://fonts.googleapis.com/css2?family=Poiret+One&display=swap">
<style>
  :root {
    --scarlet: #d3102a;
    --scarlet-deep: #b00a1f;
    --scarlet-light: #e63a4a;
    --stair-light: #ee6a72;
    --stair-mid: #e04652;
    --stair-deep: #c92a38;
    --shadow: #060102;
    --ink-white: #ffffff;
    --label-ink: #f4e9ea;
    --label-mark: #6a2a3c;
  }
  html, body {
    margin: 0;
    padding: 0;
    width: 1200px;
    height: 1200px;
    overflow: hidden;
    background: var(--shadow);
  }
  .cover {
    position: relative;
    width: 1200px;
    height: 1200px;
    overflow: hidden;
    font-family: "Poiret One", sans-serif;
    color: var(--ink-white);
  }
  .cover-photo {
    position: absolute;
    inset: 0;
    width: 1200px;
    height: 1200px;
    display: block;
  }
  .track-title {
    position: absolute;
    left: 90px;
    top: 186px;
    margin: 0;
    font-weight: 400;
    font-size: 64px;
    letter-spacing: 1px;
    white-space: nowrap;
    text-shadow: 0 0 1px var(--ink-white);
  }
  .artist-name {
    position: absolute;
    left: 112px;
    top: 982px;
    margin: 0;
    font-weight: 400;
    font-size: 58px;
    letter-spacing: 2px;
    white-space: nowrap;
    text-transform: uppercase;
  }
  .artist-name .initial {
    font-size: 86px;
  }
  .artist-name .word + .word {
    margin-left: 50px;
  }
  .imprints {
    position: absolute;
    right: 50px;
    bottom: 44px;
    display: flex;
    align-items: flex-end;
    gap: 20px;
  }
  .imprint {
    display: flex;
    flex-direction: column;
    align-items: center;
    gap: 6px;
    font-size: 15px;
    color: var(--label-ink);
    text-align: center;
    line-height: 1.15;
  }
  .imprint-mark {
    width: 44px;
    height: 54px;
    background: var(--shadow);
  }
  .imprint-mark.round {
    width: 48px;
    height: 48px;
    border-radius: 50%;
    background: var(--label-mark);
  }
</style>
</head>
<body>
<main class="cover">
  <svg class="cover-photo" viewBox="0 0 1200 1200" aria-hidden="true">
    <defs>
      <linearGradient id="wall-light" x1="0" y1="0" x2="1" y2="1">
        <stop offset="0" stop-color="var(--scarlet-deep)"/>
        <stop offset="0.5" stop-color="var(--scarlet)"/>
        <stop offset="1" stop-color="var(--scarlet-light)"/>
      </linearGradient>
      <linearGradient id="stair-tone" x1="0" y1="0" x2="1" y2="1">
        <stop offset="0" stop-color="var(--stair-deep)"/>
        <stop offset="0.5" stop-color="var(--stair-mid)"/>
        <stop offset="1" stop-color="var(--stair-light)"/>
      </linearGradient>
      <linearGradient id="silhouette-fade" x1="0" y1="0" x2="1" y2="0">
        <stop offset="0" stop-color="var(--shadow)"/>
        <stop offset="0.17" stop-color="var(--shadow)" stop-opacity="0.95"/>
        <stop offset="0.3" stop-color="var(--shadow)" stop-opacity="0"/>
      </linearGradient>
    </defs>
    <g role="img" aria-label="Photograph of a red wall beside a flight of red carpeted stairs">
      <rect width="1200" height="1200" fill="url(#wall-light)"/>
    </g>
    <g role="img" aria-label="Red carpeted staircase rising diagonally from the bottom centre to the top right corner">
      <polygon points="1165,0 1200,0 1200,1200 305,1200" fill="url(#stair-tone)"/>
    </g>
    <g role="img" aria-label="Dark blurred silhouette of a man standing at the left edge">
      <rect width="1200" height="1200" fill="url(#silhouette-fade)"/>
    </g>
  </svg>

  <h1 class="track-title">Nobody Left the Lantern Burning</h1>

  <p class="artist-name">
    <span class="word"><span class="initial">T</span>om</span><span class="word"><span class="initial">H</span>alvery</span>
  </p>

  <div class="imprints">
    <div class="imprint">
      <span class="imprint-mark"></span>
      <span>Tom<br>Halvery</span>
    </div>
    <div class="imprint">
      <span class="imprint-mark round"></span>
      <span>Milbrook &amp; Tandy<br>Records</span>
    </div>
  </div>
</main>
</body>
</html>
```